Pop up exhibition stand 2000mm (H) x 800mm (W)

I would like a simple pop up banner stand for an exhibition.

We need a pop up banner stand design for 'Brindle Forge Services'

the size is 2000mm(H) x 800mm (W)

Ad copy as follows :

[Brindle Forge logo]

From Sheet Metal To Large Sand Castings

Our Capacity and Rapid Quenching drop bottom ovens deliver precise processing.
We also serve the leading names in aerospace, automotive and advanced engineering.

Visit www.brindleforge-example.co.uk/ or call us Tel: +44 (0)1632 960318

[Put the crafted across the shires logo here, also include the text member somewhere close]

check on their website for other ideas that can help you with this project.

Target Market(s)

will be used at a trade show

Requirements
Nice to have
• modern design for UK manufacturing business

```html
<!DOCTYPE html>
<html lang="en">
<head>
<meta charset="utf-8">
<title>Brindle Forge Services – Exhibition Banner</title>
<link href="https://fonts.googleapis.com/css2?family=Open+Sans:ital,wght@0,400;0,600;0,700;1,400&display=swap" rel="stylesheet">
<style>
  :root {
    --red: #d21f36;
    --red-dark: #b5162b;
    --grey-text: #8a8a8a;
    --grey-dark: #555a60;
    --paper: #ffffff;
    --paper-soft: #f1f1f1;
    --steel-1: #c9ced3;
    --steel-2: #8e969e;
    --workshop-1: #5d7f94;
    --workshop-2: #c7ccd0;
  }
  * { margin: 0; padding: 0; box-sizing: border-box; }
  html, body { width: 1200px; height: 2576px; overflow: hidden; background: var(--paper); }
  body { font-family: "Open Sans", Arial, sans-serif; }

  .banner { width: 1200px; height: 2576px; display: flex; flex-direction: column; }

  .brand {
    height: 440px;
    background: linear-gradient(180deg, var(--paper) 0%, var(--paper-soft) 100%);
    padding: 120px 90px 0;
  }
  .brand-name {
    display: flex; align-items: center; gap: 30px;
    font-size: 74px; font-weight: 700; color: var(--red); letter-spacing: -1px;
  }
  .brand-mark { width: 70px; height: 70px; background: var(--grey-text); flex: none; }
  .brand-tagline {
    margin: 28px 0 0 100px;
    font-size: 46px; font-style: italic; color: var(--grey-dark); line-height: 1.2;
  }
  .brand-tagline .accent { color: var(--red); }

  .headline {
    height: 340px;
    display: flex; flex-direction: column; justify-content: center; align-items: center;
    font-size: 82px; line-height: 1.25; color: var(--grey-text); font-weight: 400;
  }
  .headline strong { color: var(--red); font-weight: 600; }

  .hero-photo {
    height: 840px;
    background: linear-gradient(120deg, var(--paper-soft) 0%, var(--steel-1) 55%, var(--steel-2) 100%);
  }

  .pitch {
    height: 300px; background: var(--red); color: var(--paper);
    display: flex; flex-direction: column; justify-content: center; align-items: center;
    text-align: center; font-size: 44px; line-height: 1.4; padding: 0 90px; gap: 26px;
  }
  .pitch strong { font-weight: 700; }

  .gallery { height: 300px; display: flex; gap: 10px; background: var(--paper); }
  .gallery-photo { flex: 1; }
  .gallery-photo.oven { background: linear-gradient(135deg, var(--workshop-1) 0%, var(--workshop-2) 100%); }
  .gallery-photo.inspection { background: linear-gradient(135deg, var(--steel-2) 0%, var(--paper-soft) 100%); }

  .membership {
    height: 180px; background: var(--paper-soft);
    display: flex; align-items: center; justify-content: center; gap: 40px;
    font-size: 46px; color: var(--grey-dark); letter-spacing: 1px;
  }
  .member-badge { width: 110px; height: 110px; }

  .contact {
    height: 176px; background: var(--red); color: var(--paper);
    display: flex; flex-direction: column; justify-content: center; align-items: center;
    gap: 6px;
  }
  .contact-web { font-size: 60px; font-weight: 600; }
  .contact-phone { font-size: 42px; }
</style>
</head>
<body>
<main class="banner">
  <header class="brand">
    <div class="brand-name"><span class="brand-mark"></span>Brindle Forge Services</div>
    <p class="brand-tagline">the solution in <span class="accent">aluminium heat treatment</span></p>
  </header>

  <h1 class="headline">
    <span>From <strong>Sheet Metal</strong></span>
    <span>To <strong>Large Sand Castings</strong></span>
  </h1>

  <div class="hero-photo" role="img" aria-label="Photograph of a staff member in a white shirt and red tie beside machined aluminium blocks in the workshop"></div>

  <section class="pitch">
    <p>Our <strong>Capacity</strong> and <strong>Rapid Quenching</strong> drop bottom ovens deliver <strong>precise</strong> processing.</p>
    <p>We also serve the <strong>leading</strong> names in aerospace, automotive and advanced engineering.</p>
  </section>

  <section class="gallery">
    <div class="gallery-photo oven" role="img" aria-label="Photograph of a large blue heat treatment oven with a metal ring"></div>
    <div class="gallery-photo inspection" role="img" aria-label="Photograph of an engineer inspecting a treated component"></div>
  </section>

  <section class="membership">
    <span>MEMBER OF</span>
    <svg class="member-badge" viewBox="0 0 110 110" role="img" aria-label="crafted across the shires membership badge">
      <circle cx="55" cy="55" r="52" fill="var(--red)"/>
    </svg>
  </section>

  <footer class="contact">
    <span class="contact-web">www.brindleforge-example.co.uk</span>
    <span class="contact-phone">call us: +44 (0)1632 960318</span>
  </footer>
</main>
</body>
</html>
```